BramliVex a new start up looking for packaging design for it's organic Cold pressed Peanut oil.

We require a labelling design for a new company based in the UK called ''BramliVex''. We will be launching Organic cold pressed peanut oil. We would like a design that is simple yet very catchy and not boring.

Target Market(s)
General consumers and healthy eaters, Vegan friendly

Colors
Designer to choose colors to be used in the design.

Must have
• Refer to Packaging document information for labelling.
• Type of bottle 250 ML Selvane bottle (refer to Bottle Picture doc.)
• Must have the "BramliVex" logo stamped somewhere on the front of the package (refer to the Logo document)
• Sleek and appetising design
• Neutral colors possible accents with logo colors
• Claims: Organic, Vegan, High in Monounsaturated fat, High in Poly-unsaturated fat(all this in front of the package)
• Made in the uk logo, and EU organic logo
• Social Media Icons (Pictaloom,Chatterdesk) as well as website (Bramlivex.co.uk)
• Space reserved at the back of the package for barcode and best before date to be printed on.
Be nice to have: picture of the product on the background if possible
Updates

Need extra days to review

Target Market(s)

Font styles to use
Serif
Sans Serif
Decorative
Script

Requirements
Must have

• • Refer to Packaging document information for labelling.

```html
<!DOCTYPE html>
<html lang="en">
<head>
<meta charset="UTF-8">
<title>BramliVex Organic Peanut Oil Label</title>
<link href="https://fonts.googleapis.com/css2?family=Oswald:wght@300;400;500;600&display=swap" rel="stylesheet">
<style>
  :root {
    --stage: #a89bab;
    --tan-light: #e4c59d;
    --tan-dark: #c49a5e;
    --cocoa: #2a0e0d;
    --cream: #f6e8de;
    --ink: #2a0e0d;
    --leaf: #7fd13a;
    --flag: #2c3f8a;
    --social-a: #c53c8a;
    --social-b: #1b2f6b;
    --nut: #e8b865;
  }
  * { box-sizing: border-box; margin: 0; padding: 0; }
  html, body { width: 1200px; height: 800px; overflow: hidden; }
  body {
    background: var(--stage);
    font-family: "Oswald", "Arial Narrow", sans-serif;
    color: var(--ink);
    position: relative;
  }
  .label {
    position: absolute;
    left: 172px; top: 8px;
    width: 856px; height: 784px;
    background: linear-gradient(135deg, var(--tan-light) 0%, var(--tan-dark) 100%);
    overflow: hidden;
  }
  .label__base { position: absolute; inset: 0; }
  .abs { position: absolute; }

  /* nutrition table */
  .nutrition {
    left: 34px; top: 97px; width: 191px;
    border: 2px solid var(--ink);
    font-size: 13px; font-weight: 300;
  }
  .nutrition__title {
    background: var(--cocoa); color: var(--cream);
    text-align: center; font-size: 16px; font-weight: 400;
    height: 20px; line-height: 20px;
  }
  .nutrition__row {
    display: flex; justify-content: space-between;
    height: 25px; line-height: 24px; padding: 0 2px;
    border-top: 2px solid var(--ink);
  }
  .nutrition__row--sub { padding-left: 16px; padding-right: 8px; border-top-width: 1px; }

  /* logo & illustrations */
  .logo-main {
    left: 310px; top: 40px; width: 250px;
    text-align: center; font-size: 54px; font-weight: 600;
    letter-spacing: 1px; line-height: 1;
  }
  .mascot {
    left: 380px; top: 100px; width: 100px; height: 140px;
    border-radius: 48px 48px 36px 36px;
    background: radial-gradient(circle at 50% 40%, #a86a3e, #3a1810);
  }
  .peanuts {
    left: 338px; top: 248px; width: 196px; height: 160px;
    border-radius: 50%;
    background: radial-gradient(ellipse at 45% 50%, #f4cf82, #d99b45 70%, rgba(120,170,60,.8));
  }

  /* right column */
  .logo-small {
    left: 690px; top: 118px; width: 110px;
    text-align: center; font-size: 24px; font-weight: 600;
  }
  .mascot-small {
    left: 728px; top: 148px; width: 30px; height: 54px;
    border-radius: 14px;
    background: radial-gradient(circle at 50% 40%, #a86a3e, #3a1810);
  }
  .visit { left: 643px; top: 217px; font-size: 13px; font-weight: 400; }
  .site {
    left: 643px; top: 236px; font-size: 23px; font-weight: 600;
    display: flex; align-items: center; gap: 4px;
  }
  .site__globe { width: 15px; height: 15px; border-radius: 50%; background: var(--ink); }
  .find-us {
    left: 646px; top: 297px; width: 84px; height: 27px;
    background: var(--cocoa); color: var(--cream);
    text-align: center; line-height: 27px; font-size: 16px;
  }
  .social { top: 333px; display: flex; align-items: center; gap: 3px; font-size: 11px; font-weight: 500; }
  .social__dot { width: 34px; height: 34px; border-radius: 50%; }
  .badge { width: 80px; height: 80px; border-radius: 50%; }
  .badge--uk { left: 640px; top: 434px; background: var(--flag); border: 3px solid var(--cream); }
  .badge--organic { left: 733px; top: 434px; background: var(--leaf); border: 3px solid var(--cream); }

  /* back copy */
  .ingredients { left: 33px; top: 486px; width: 220px; color: var(--cream); }
  .ingredients h3 { font-size: 17px; font-weight: 500; }
  .ingredients p { font-size: 13px; font-weight: 300; line-height: 23px; }
  .ingredients .allergy { margin-top: 20px; }

  /* claims */
  .claims { left: 288px; top: 520px; width: 250px; font-size: 21px; font-weight: 400; line-height: 30px; }
  .claims__row { display: flex; align-items: center; gap: 6px; }
  .claims__row--split { justify-content: space-between; }
  .claims__item { display: flex; align-items: center; gap: 6px; }
  .claims__bullet { width: 16px; height: 9px; border-radius: 5px; background: var(--nut); border: 1px solid #a56f2a; }

  .volume {
    left: 518px; top: 690px; width: 102px; height: 50px;
    border-radius: 50%; background: var(--cream);
    text-align: center; line-height: 50px; font-size: 21px; font-weight: 500;
  }
  .best-before {
    left: 643px; top: 618px; width: 169px; height: 29px;
    background: var(--cream); text-align: center; line-height: 29px;
    font-size: 16px; font-weight: 500;
  }
  .barcode-space {
    left: 643px; top: 659px; width: 175px; height: 83px;
    background: var(--cream); text-align: center; line-height: 83px;
    font-size: 17px; font-weight: 500;
  }
</style>
</head>
<body>
<main class="label">
  <svg class="label__base" viewBox="0 0 856 784" aria-hidden="true">
    <path d="M0 345 L370 705 Q410 750 450 715 L856 343 L856 784 L0 784 Z" fill="var(--cocoa)"/>
  </svg>

  <section class="abs nutrition">
    <div class="nutrition__title">Nutrition Information</div>
    <div class="nutrition__row"><span>Typical values</span><span>per 100g</span></div>
    <div class="nutrition__row"><span>Energy</span><span>kJ896/kCal3685</span></div>
    <div class="nutrition__row"><span>Fat</span><span>100g</span></div>
    <div class="nutrition__row nutrition__row--sub"><span>Of which Saturated</span><span>19.7g</span></div>
    <div class="nutrition__row nutrition__row--sub"><span>Mono-unsaturated</span><span>36.4g</span></div>
    <div class="nutrition__row nutrition__row--sub"><span>Poly-unsaturated</span><span>43.4g</span></div>
    <div class="nutrition__row"><span>Protein</span><span>0.1g</span></div>
    <div class="nutrition__row"><span>Carbohydrate</span><span>&lt;0.5g</span></div>
    <div class="nutrition__row nutrition__row--sub"><span>Of which sugar</span><span>&lt;0.1g</span></div>
    <div class="nutrition__row"><span>Fibre</span><span>&lt;0.5</span></div>
  </section>

  <div class="abs logo-main">BramliVex</div>
  <div class="abs mascot" role="img" aria-label="Brand mascot illustration"></div>
  <div class="abs peanuts" role="img" aria-label="Illustration of peanuts in shells with green leaves"></div>

  <div class="abs logo-small">BramliVex</div>
  <div class="abs mascot-small" role="img" aria-label="Small brand mascot illustration"></div>
  <p class="abs visit">For more details please visit us:</p>
  <p class="abs site"><span class="site__globe"></span>Bramlivex.co.uk</p>
  <div class="abs find-us">Find Us On</div>
  <div class="abs social" style="left:644px"><span class="social__dot" style="background:var(--social-a)"></span>Pictaloom</div>
  <div class="abs social" style="left:728px"><span class="social__dot" style="background:var(--social-b)"></span>Chatterdesk</div>
  <div class="abs badge badge--uk" role="img" aria-label="Made in UK badge"></div>
  <div class="abs badge badge--organic" role="img" aria-label="Organic certification badge"></div>

  <section class="abs ingredients">
    <h3>Ingredients</h3>
    <p>100% Organic peanut oil</p>
    <h3 class="allergy">Allergy Advice:</h3>
    <p>Peanuts are packed on premises that handles cereals, nuts (including peanuts), soya, sesame &amp; products containing gluten.</p>
  </section>

  <section class="abs claims">
    <div class="claims__row claims__row--split">
      <span class="claims__item"><span class="claims__bullet"></span>Organic</span>
      <span class="claims__item"><span class="claims__bullet"></span>Vegan</span>
    </div>
    <div class="claims__row"><span class="claims__bullet"></span>High in Monounsaturated Fat</div>
    <div class="claims__row"><span class="claims__bullet"></span>High in Poly-Unsaturated Fat</div>
  </section>

  <div class="abs volume">250 ML</div>
  <div class="abs best-before">Best Before Date</div>
  <div class="abs barcode-space">BARCODE</div>
</main>
</body>
</html>
```